Need designers to make a boring check list funky and fun

We are an executive rental company based in Sydney. We deal in fully furnished properties for both short and long term bookings. We have a check list for home owners to help them prepare their home for guests.
We are looking for an interesting design which makes the mundane tasks seem both fun and enjoyable.
Target Market(s)
single, couples and families where they are dual income households. Highly educated, high powered jobs with little to no time and are stressed needing a break, but also needing to pay the mortgage.
Industry/Entity Type
It Company
Colors
Designer to choose colors to be used in the design.
Requirements
Must have
- images of house rooms, clean.
- our logo on it
Nice to have
- icons for each section ie person swimming for a pool
Should not have
- just text no images

```html
<!DOCTYPE html>
<html lang="en">
<head>
<meta charset="utf-8">
<title>Korimo Properties – Check list for Holiday Owners</title>
<link rel="stylesheet" href="https://fonts.googleapis.com/css2?family=Barlow:wght@400;500;600;700&family=Tinos&display=swap">
<style>
  :root{
    --brand-red:#e5214c;
    --brand-red-soft:#ea4a6c;
    --ink:#2e2e2e;
    --ink-soft:#444;
    --panel-grey:#ececec;
    --rule:#c9c9c9;
    --frame:#b9b9b9;
    --white:#ffffff;
    --box-dark:#3b3b3b;
  }
  *{box-sizing:border-box;margin:0;padding:0}
  html,body{width:1098px;height:1200px;overflow:hidden;background:var(--white)}
  body{position:relative;font-family:"Barlow",Arial,sans-serif;color:var(--ink)}

  .page{position:absolute;width:338px;height:478px;background:var(--white);overflow:hidden}
  .spread{position:absolute;border:1px solid var(--frame)}
  .spread--covers{left:69px;top:62px;width:677px;height:479px}
  .spread--inside{left:69px;top:618px;width:677px;height:479px}
  .page--left{left:0;top:0;border-right:1px solid var(--frame)}
  .page--right{left:338px;top:0}

  .top-band{position:absolute;left:0;top:0;width:100%;height:22px;background:linear-gradient(90deg,var(--brand-red-soft),var(--brand-red))}

  .room-icon{position:absolute;left:19px;width:39px;height:39px;border-radius:50%;background:var(--brand-red)}
  .section-title{position:absolute;left:68px;font-size:8.6px;font-weight:600;color:var(--ink);letter-spacing:.1px}
  .checklist{position:absolute;left:68px;width:184px;list-style:none}
  .checklist li{position:relative;padding-left:9px;font-size:4.9px;line-height:6.2px;color:var(--ink-soft);margin-bottom:3.2px}
  .checklist li::before{content:"";position:absolute;left:1px;top:2px;width:2.2px;height:2.2px;border-radius:50%;background:var(--brand-red)}
  .rule{position:absolute;left:68px;width:190px;height:1px;background:var(--rule)}

  .final-panel{position:absolute;left:0;top:263px;width:100%;height:215px;background:var(--panel-grey)}
  .final-badge{position:absolute;left:17px;top:280px;width:40px;height:40px}
  .final-title{position:absolute;left:68px;top:281px;font-size:8.6px;line-height:10px;font-weight:600;color:var(--brand-red)}

  .brand-lockup{position:absolute;left:101px;top:397px;height:24px;display:flex;align-items:center;gap:4px}
  .brand-lockup .mark{width:24px;height:24px;background:var(--brand-red)}
  .brand-lockup .name{height:24px;padding:0 9px;display:flex;align-items:center;background:var(--brand-red);color:var(--white);font-size:7px;letter-spacing:.9px;font-weight:400}

  .contact{position:absolute;left:0;width:100%;text-align:center}
  .contact .url{font-size:11.5px;font-weight:700;color:var(--brand-red);letter-spacing:.2px}
  .contact .phone{margin-top:3px;font-size:7px;font-weight:500;color:var(--ink)}
  .contact .hours{font-size:6px;font-weight:500;color:var(--ink);line-height:7px}

  .cover-brand{position:absolute;left:0;top:31px;width:100%;text-align:center}
  .cover-brand .mark{display:block;margin:0 auto;width:44px;height:44px;background:var(--brand-red)}
  .cover-brand .name{margin-top:15px;font-size:8.2px;letter-spacing:2.4px;color:var(--ink-soft);font-weight:500}
  .cover-brand .divider{width:110px;height:1px;background:var(--brand-red);margin:3px auto 4px}
  .cover-brand .tagline{font-size:8.2px;letter-spacing:1.2px;color:var(--ink-soft)}

  .cover-panel{position:absolute;left:0;top:144px;width:100%;height:277px;background:var(--brand-red)}
  .cover-panel h1{position:absolute;left:0;top:14px;width:100%;text-align:center;font-size:10.4px;font-weight:600;color:var(--white);letter-spacing:.2px}
  .tick-box{position:absolute;left:63px;width:46px;height:46px}
  .cover-list{position:absolute;left:131px;top:70px;width:112px;list-style:none}
  .cover-list li{font-size:5.6px;line-height:6.6px;color:#ffe3e9;margin-bottom:5px}
  .cover-foot{position:absolute;left:0;top:421px;width:100%;height:57px;background:var(--panel-grey)}

  .caption{position:absolute;font-family:"Tinos","Times New Roman",serif;font-size:15.5px;color:#222}
  .spec{position:absolute;left:852px;top:194px;font-size:22px;line-height:27.5px;color:#1e1e1e;font-weight:500;letter-spacing:.2px}
</style>
</head>
<body>

<div class="spread spread--covers">
  <section class="page page--left back-cover">
    <div class="top-band"></div>

    <div class="room-icon" style="top:36px" role="img" aria-label="Pool icon: swimming pool ladder"></div>
    <h3 class="section-title" style="top:36px">Pool</h3>
    <ul class="checklist" style="top:50px">
      <li>Safety</li>
      <li>Provide fire extinguisher, fire blanket and first aid kit</li>
      <li>Repair leaking taps, broken tiles, etc</li>
      <li>Patch and holes in walls</li>
      <li>Check smoke alarms functioning</li>
    </ul>
    <div class="rule" style="top:106px"></div>

    <div class="room-icon" style="top:118px" role="img" aria-label="Insurance icon: person protecting a house"></div>
    <h3 class="section-title" style="top:112px">Insurance</h3>
    <ul class="checklist" style="top:126px">
      <li>Empty Pantry (spices, salt and pepper and unopened tins can remain if you don't mind guests using them)</li>
      <li>Thoroughly clean oven and microwave.</li>
      <li>Wipe out cupboards and ensure all hinges are in working order</li>
      <li>Clean out fridge and freezer. Wipe all surfaces.</li>
      <li>Check all appliances are in working order and clean.</li>
      <li>Run Dishwasher with a dishwashing cleaner in it. Fill up the rinse aid.</li>
      <li>Remove any alcohol</li>
      <li>Remove any sentimental or expensive crockery items</li>
      <li>Check all crockery is not chipped or damaged.</li>
      <li>Leave crockery and cutlery for twice the maximum number of guests</li>
      <li>Think of getting a glass top to protect tables and cabinets especially if they are French polished.</li>
    </ul>

    <div class="final-panel"></div>
    <svg class="final-badge" viewBox="0 0 40 40" role="img" aria-label="Approval seal with tick">
      <circle cx="20" cy="20" r="17" fill="none" stroke="var(--brand-red)" stroke-width="3"/>
      <path d="M12 20 l6 6 l11 -12" fill="none" stroke="var(--brand-red)" stroke-width="3.5" stroke-linecap="round" stroke-linejoin="round"/>
    </svg>
    <div class="final-title">Your Almost there....<br>Final bits</div>
    <ul class="checklist" style="top:313px">
      <li>Provide 4 sets of keys for Korimo Properties</li>
      <li>Arrange rubbish to be placed out on street when required (Korimo can arrange this at a fee)</li>
      <li>Let Korimo know of any areas which could be affected by heavy rain</li>
      <li>Cleaners come in to set up the property prior to guests arrival</li>
    </ul>

    <div class="brand-lockup">
      <span class="mark"></span>
      <span class="name">KORIMO PROPERTIES</span>
    </div>
    <div class="contact" style="top:425px;left:-6px">
      <div class="url">www.korimo.com.au</div>
      <div class="phone">+61 400 123 456</div>
      <div class="hours">business hours</div>
    </div>
  </section>

  <section class="page page--right front-cover">
    <div class="cover-brand">
      <span class="mark"></span>
      <div class="name">KORIMO PROPERTIES</div>
      <div class="divider"></div>
      <div class="tagline">HOMES FOR EASY STAYS</div>
    </div>

    <div class="cover-panel">
      <h1>Check list for Holiday Owners</h1>
      <svg class="tick-box" style="top:68px" viewBox="0 0 46 46" aria-hidden="true">
        <rect x="0" y="2" width="44" height="44" rx="5" fill="var(--box-dark)"/>
        <path d="M9 24 l10 10 l22 -28" fill="none" stroke="var(--white)" stroke-width="6" stroke-linecap="round" stroke-linejoin="round"/>
      </svg>
      <svg class="tick-box" style="top:135px" viewBox="0 0 46 46" aria-hidden="true">
        <rect x="0" y="2" width="44" height="44" rx="5" fill="var(--box-dark)"/>
        <path d="M9 24 l10 10 l22 -28" fill="none" stroke="var(--white)" stroke-width="6" stroke-linecap="round" stroke-linejoin="round"/>
      </svg>
      <svg class="tick-box" style="top:202px" viewBox="0 0 46 46" aria-hidden="true">
        <rect x="0" y="2" width="44" height="44" rx="5" fill="var(--box-dark)"/>
        <path d="M9 24 l10 10 l22 -28" fill="none" stroke="var(--white)" stroke-width="6" stroke-linecap="round" stroke-linejoin="round"/>
      </svg>
      <ul class="cover-list">
        <li>Provide spare light bulbs and batteries for all the remotes</li>
        <li>Put felt pads under furniture to protect the floor from scratching</li>
        <li>Put coasters under any furniture with wheels</li>
        <li>Remove any personal items such as photos, and sentimental items</li>
        <li>Lock up all linen including tea towels</li>
        <li>Unplug any home phones</li>
        <li>Leave modem in an area accessible by the guests.</li>
        <li>Network name and Password to be on sticker on device</li>
        <li>Ensure Internet is unlimited and the network name and Password are provided to Korimo Properties</li>
        <li>Property to be pest sprayed for cockroaches, and ants</li>
      </ul>
    </div>

    <div class="cover-foot"></div>
    <div class="contact" style="top:425px">
      <div class="url">www.korimo.com.au</div>
      <div class="phone">+61 400 123 456</div>
      <div class="hours">business hours</div>
    </div>
  </section>
</div>

<div class="caption" style="left:202px;top:543px">back cover</div>
<div class="caption" style="left:544px;top:543px">Front cover</div>

<div class="spread spread--inside">
  <section class="page page--left inside-page">
    <div class="top-band"></div>
    <div class="room-icon" style="top:37px" role="img" aria-label="Living room icon: sofa, lamp and picture"></div>
    <h3 class="section-title" style="top:36px">Living Room</h3>
    <ul class="checklist" style="top:50px">
      <li>Check all furniture, rugs, carpet and floors have no rips, tears, stains and are in good condition.</li>
      <li>Wash/Steam Clean cushion covers</li>
      <li>Steam clean any upholstery if it requires it</li>
      <li>If you have an animal all carpet, upholstery and rugs will need to be steam cleaned prior to guests arrival.</li>
      <li>Put in new batteries to all remotes, smoke alarms and other such devices.</li>
      <li>Detailed instructions on how to work all electronics (in guest handbook template we provide)</li>
      <li>Pack away any faulty electrical equipment</li>
      <li>Log out of all devices and set up a guest password for StreamBox, FlixOn and cable TV accounts. (Password to go in guests manual and a sticker to go on the device)</li>
    </ul>
    <div class="rule" style="top:166px"></div>

    <div class="room-icon" style="top:178px" role="img" aria-label="Kitchen icon: cupboards and appliances"></div>
    <h3 class="section-title" style="top:171px">Kitchen</h3>
    <ul class="checklist" style="top:186px">
      <li>Empty Pantry (spices, salt and pepper and unopened tins can remain if you don't mind guests using them)</li>
      <li>Thoroughly clean oven and microwave.</li>
      <li>Wipe out cupboards and ensure all hinges are in working order</li>
      <li>Clean out fridge and freezer. Wipe all surfaces.</li>
      <li>Check all appliances are in working order and clean.</li>
      <li>Run Dishwasher with a dishwashing cleaner in it. Fill up the rinse aid.</li>
      <li>Remove any alcohol</li>
      <li>Remove any sentimental or expensive crockery items</li>
      <li>Check all crockery is not chipped or damaged.</li>
      <li>Leave crockery and cutlery for twice the maximum number of guests</li>
      <li>Think of getting a glass top to protect tables and cabinets especially if they are French polished.</li>
    </ul>
    <div class="rule" style="top:313px"></div>

    <div class="room-icon" style="top:319px" role="img" aria-label="Stairs icon: staircase with railing"></div>
    <h3 class="section-title" style="top:318px">Stairs</h3>
    <ul class="checklist" style="top:333px">
      <li>Check the balustrade and railings are secure</li>
      <li>Repair any loose carpet</li>
    </ul>
    <div class="rule" style="top:377px"></div>

    <div class="room-icon" style="top:388px" role="img" aria-label="Bedroom icon: bed and bedside table"></div>
    <h3 class="section-title" style="top:387px">Bedrooms</h3>
    <ul class="checklist" style="top:402px">
      <li>Clear ½ the robes for the guests to use in each of the bedrooms. Lock the sections you are using.</li>
      <li>Clear out draws and bedside tables</li>
      <li>Leave new mattress protectors, pillow protectors for each pillow, doona's, doona protectors, extra blankets and pillows including all sofa beds and trundle beds.</li>
    </ul>
  </section>

  <section class="page page--right inside-page">
    <div class="top-band"></div>
    <div class="room-icon" style="top:37px" role="img" aria-label="Living room icon: sofa, lamp and picture"></div>
    <h3 class="section-title" style="top:36px">Living Room</h3>
    <ul class="checklist" style="top:50px">
      <li>Check all furniture, rugs, carpet and floors have no rips, tears, stains and are in good condition.</li>
      <li>Wash/Steam Clean cushion covers</li>
      <li>Steam clean any upholstery if it requires it</li>
      <li>If you have an animal all carpet, upholstery and rugs will need to be steam cleaned prior to guests arrival.</li>
      <li>Put in new batteries to all remotes, smoke alarms and other such devices.</li>
      <li>Detailed instructions on how to work all electronics (in guest handbook template we provide)</li>
      <li>Pack away any faulty electrical equipment</li>
      <li>Log out of all devices and set up a guest password for StreamBox, FlixOn and cable TV accounts. (Password to go in guests manual and a sticker to go on the device)</li>
    </ul>
    <div class="rule" style="top:166px"></div>

    <div class="room-icon" style="top:178px" role="img" aria-label="Kitchen icon: cupboards and appliances"></div>
    <h3 class="section-title" style="top:171px">Kitchen</h3>
    <ul class="checklist" style="top:186px">
      <li>Empty Pantry (spices, salt and pepper and unopened tins can remain if you don't mind guests using them)</li>
      <li>Thoroughly clean oven and microwave.</li>
      <li>Wipe out cupboards and ensure all hinges are in working order</li>
      <li>Clean out fridge and freezer. Wipe all surfaces.</li>
      <li>Check all appliances are in working order and clean.</li>
      <li>Run Dishwasher with a dishwashing cleaner in it. Fill up the rinse aid.</li>
      <li>Remove any alcohol</li>
      <li>Remove any sentimental or expensive crockery items</li>
      <li>Check all crockery is not chipped or damaged.</li>
      <li>Leave crockery and cutlery for twice the maximum number of guests</li>
      <li>Think of getting a glass top to protect tables and cabinets especially if they are French polished.</li>
    </ul>
    <div class="rule" style="top:313px"></div>

    <div class="room-icon" style="top:319px" role="img" aria-label="Stairs icon: staircase with railing"></div>
    <h3 class="section-title" style="top:318px">Stairs</h3>
    <ul class="checklist" style="top:333px">
      <li>Check the balustrade and railings are secure</li>
      <li>Repair any loose carpet</li>
    </ul>
    <div class="rule" style="top:377px"></div>

    <div class="room-icon" style="top:388px" role="img" aria-label="Bedroom icon: bed and bedside table"></div>
    <h3 class="section-title" style="top:387px">Bedrooms</h3>
    <ul class="checklist" style="top:402px">
      <li>Clear ½ the robes for the guests to use in each of the bedrooms. Lock the sections you are using.</li>
      <li>Clear out draws and bedside tables</li>
      <li>Leave new mattress protectors, pillow protectors for each pillow, doona's, doona protectors, extra blankets and pillows including all sofa beds and trundle beds.</li>
    </ul>
  </section>
</div>

<div class="caption" style="left:365px;top:1099px">Inside pages</div>

<div class="spec">
  A4 Document<br>
  4 pages<br>
  1 x A3 folded once<br>
  2 colours
</div>

</body>
</html>
```